Stationary Design needed for luxorious bespoke tailor

We need a design for our stationary items like businescards, letters, envelope and letter head / Signature for email. Our company "LE CORVAN" sells exclusively and luxourious bespoke garments and accessories for men. The desgins of letterhead, envelope and business card shoulderstand communicate luxury, high quality and good taste. We would like our logo to be used on the designs.

Target Market(s)

Gentleman with a high aproach and exclusive and luxourious suits and shirts, grooms, businesman,

Industry/Entity Type

It Company

Font styles to use
Sans Serif

Colors
ec1f27
ffffff

Requirements
Must have
• Logo, Companies name and adress, contactName internet & email, phone number line / mobile, VAT Nr. On Business Card frontpage only logo and name, adress companies on backpage. No VAT and Companies ID there. Company data; LE CORVAN AG Wiesenrain 42 4057 Basel Switzerland VAT: CHE 472 916 304 Tax Tel 41 61 594 17 36 Mobile 41 79 842 06 91 www.korvanmode.ch info@korvanmode.com.
Nice to have
• -Name And phone numbers need to be able to change (for different coworkers ...)
Should not have
• no VAT in Business Card

```html
<!DOCTYPE html>
<html lang="en">
<head>
<meta charset="utf-8">
<title>LE CORVAN – Business Card</title>
<link rel="stylesheet" href="https://fonts.googleapis.com/css2?family=Montserrat:wght@400;600;700&display=swap">
<style>
  :root {
    --brand-red: #ec1f27;
    --paper-white: #ffffff;
    --card-black: #070404;
    --backdrop: #3b3b3b;
    --text-dark: #1a1a1a;
    --rule-light: #d8d8d8;
  }
  * { margin: 0; padding: 0; box-sizing: border-box; }
  html, body {
    width: 1200px; height: 987px; overflow: hidden;
    background: var(--backdrop);
    font-family: "Montserrat", sans-serif;
  }
  .stage { position: relative; width: 1200px; height: 987px; }
  .card {
    position: absolute; left: 293px; width: 615px; height: 352px;
    box-shadow: 0 4px 10px rgba(0,0,0,0.35);
  }
  .card-front { top: 130px; background: var(--paper-white); text-align: center; }
  .card-back { top: 505px; background: var(--card-black); color: var(--paper-white); }

  .brand-name {
    position: absolute; left: 0; right: 0; top: 272px;
    font-weight: 600; font-size: 50px; letter-spacing: 2px;
    color: var(--text-dark); line-height: 1;
  }
  .person-name {
    position: absolute; left: 0; right: 0; top: 384px;
    font-weight: 700; font-size: 23px; color: var(--brand-red); letter-spacing: 0.5px;
  }
  .person-role {
    position: absolute; left: 0; right: 0; top: 412px;
    font-size: 17px; color: var(--text-dark);
  }
  .card-front .brand-name { top: 142px; }
  .card-front .person-name { top: 254px; }
  .card-front .person-role { top: 282px; }

  .company-address {
    position: absolute; left: 0; right: 0; top: 204px;
    text-align: center; font-size: 17px; letter-spacing: 0.3px;
  }
  .rule {
    position: absolute; left: 34px; right: 36px; height: 1px;
    background: var(--rule-light);
  }
  .rule-top { top: 238px; }
  .rule-bottom { top: 318px; }
  .contact-list {
    position: absolute; top: 254px; list-style: none;
    font-size: 17px; line-height: 24px;
  }
  .contact-list li { display: flex; align-items: center; gap: 8px; }
  .contact-phones { left: 40px; }
  .contact-online { right: 38px; }
  .contact-online li { justify-content: flex-end; }
  .icon { width: 15px; height: 15px; fill: var(--brand-red); flex: none; }
</style>
</head>
<body>
<div class="stage">
  <section class="card card-front">
    <div class="brand-name">LE CORVAN</div>
    <div class="person-name">ELIAS BRUNNER</div>
    <div class="person-role">CEO/Founder</div>
  </section>

  <section class="card card-back">
    <p class="company-address">LE CORVAN AG, Wiesenrain 42, 4057 Basel , Switzerland</p>
    <div class="rule rule-top"></div>
    <ul class="contact-list contact-phones">
      <li>
        <svg class="icon" viewBox="0 0 16 16"><path d="M3.5 1l2.6 3-1.3 2.1c.9 2 2.4 3.5 4.4 4.4l2.1-1.3 3 2.6-1.6 2.5C6.7 14.8 1.2 9.3 1 3.3z"/></svg>
        <span>+41 61 594 17 36</span>
      </li>
      <li>
        <svg class="icon" viewBox="0 0 16 16"><path d="M4 0h8a1 1 0 0 1 1 1v14a1 1 0 0 1-1 1H4a1 1 0 0 1-1-1V1a1 1 0 0 1 1-1zm.8 2v10.5h6.4V2zM8 13.3a.9.9 0 1 0 0 1.8.9.9 0 0 0 0-1.8z"/></svg>
        <span>+41 79 842 06 91</span>
      </li>
    </ul>
    <ul class="contact-list contact-online">
      <li>
        <span>info@korvanmode.com</span>
        <svg class="icon" viewBox="0 0 16 16"><path d="M1 4h14v1L8 9.5 1 5zm0 2.5l7 4.5 7-4.5V13H1z"/></svg>
      </li>
      <li>
        <span>www.korvanmode.ch</span>
        <svg class="icon" viewBox="0 0 16 16"><circle cx="8" cy="8" r="7"/><path d="M1 8h14M8 1c-2.5 2-2.5 12 0 14M8 1c2.5 2 2.5 12 0 14" stroke="#070404" stroke-width="1" fill="none"/></svg>
      </li>
    </ul>
    <div class="rule rule-bottom"></div>
  </section>
</div>
</body>
</html>
```